Corvant Systems Business Card

Create an appealing and elegant Business card for corvant systems. Include logo and use related colors from website, be creative. Include Business name, my name, tile, address, contacts, address, and social media contacts if possible. Logo PSD file is attached.

Bleed Area: 3.46" x 2.32"
Trim: 3.3" x 2.16"
Safe Area: 3.14" x 2.02"

Save files as vector-based PDF with outlined text and PNG.
No crop marks
CMYK color setting

Business Card Info:

Corvant Systems

Dennis Halvorsen
Owner

512 Brindlemoor Rd Unit C
Merrow Hollow, QX 02871
t. 1.888.555.0162
e. dennis.h@corvantsys.example
w. www.corvantsys.example

facebook. www.facebook.com/CorvantSys
twitter. twitter.com/corvantsys
pinterest. www.pinterest.com/corvantsys/

Target Market(s)

Business Owners and Partners

Industry/Entity Type

Business

Requirements
Must have
• Logo and related colors from website

```html
<!DOCTYPE html>
<html lang="en">
<head>
<meta charset="utf-8">
<title>Corvant Systems Business Card</title>
<link href="https://fonts.googleapis.com/css2?family=Open+Sans:wght@400;600&display=swap" rel="stylesheet">
<style>
  :root {
    --backdrop: #e7e7e9;
    --card: #f4f4f4;
    --band-top: #4f86bd;
    --band-bottom: #2f5f93;
    --ink: #1c1c1e;
    --ink-soft: #55585e;
    --accent: #3b70aa;
    --rule: #a9abaf;
    --icon: #cfe0f2;
  }
  * { box-sizing: border-box; margin: 0; padding: 0; }
  html, body { width: 1200px; height: 873px; overflow: hidden; }
  body {
    background: var(--backdrop);
    font-family: "Open Sans", Arial, sans-serif;
    display: flex;
    align-items: center;
    justify-content: center;
    gap: 40px;
  }
  .card {
    position: relative;
    width: 540px;
    height: 354px;
    background: var(--card);
    border-radius: 22px;
    overflow: hidden;
    box-shadow: 0 4px 14px rgba(0,0,0,0.15);
  }
  .card__band {
    position: absolute;
    left: 0; top: 0; bottom: 0;
    width: 36px;
    background: linear-gradient(90deg, var(--band-top), var(--band-bottom));
  }
  .social-icons {
    position: absolute;
    left: 8px; top: 38px;
    display: flex;
    flex-direction: column;
    gap: 9px;
  }
  .social-icons svg { display: block; }

  .contact {
    position: absolute;
    left: 54px; top: 36px;
    width: 226px;
  }
  .contact__name { font-weight: 600; font-size: 16px; color: var(--ink); }
  .contact__title { font-size: 11px; color: var(--accent); letter-spacing: 0.5px; margin-bottom: 12px; }
  .contact__line { font-size: 12px; color: var(--ink); line-height: 1.55; white-space: nowrap; }
  .contact__line--web { color: var(--accent); font-weight: 600; }
  .contact__line--social { color: var(--ink-soft); font-size: 11px; }

  .card__divider {
    position: absolute;
    left: 290px; top: 36px; bottom: 36px;
    width: 1px;
    background: var(--rule);
  }
  .identity {
    position: absolute;
    left: 310px; top: 80px;
    width: 210px;
  }
  .wordmark {
    font-size: 25px;
    font-weight: 400;
    color: var(--ink);
    line-height: 1.1;
    margin-bottom: 18px;
  }
  .address { font-size: 14px; color: var(--ink); line-height: 1.45; }

  .card--front .wordmark {
    position: absolute;
    left: 36px; right: 0; top: 0; bottom: 0;
    display: flex;
    align-items: center;
    justify-content: center;
    font-size: 44px;
    margin: 0;
  }
</style>
</head>
<body>
  <section class="card card--back" aria-label="Business card back">
    <div class="card__band">
      <div class="social-icons">
        <svg width="20" height="20" viewBox="0 0 20 20"><circle cx="10" cy="10" r="8.5" fill="none" stroke="var(--icon)" stroke-width="1.3"/><path d="M7 6.5c0 3.5 3 6.5 6.5 6.5l.8-1.6-1.8-.9-.9.9c-1-.5-2-1.5-2.5-2.5l.9-.9-.9-1.8z" fill="var(--icon)"/></svg>
        <svg width="20" height="20" viewBox="0 0 20 20"><circle cx="10" cy="10" r="8.5" fill="none" stroke="var(--icon)" stroke-width="1.3"/><rect x="5.5" y="7" width="9" height="6" fill="none" stroke="var(--icon)"/><path d="M5.5 7l4.5 3.5L14.5 7" fill="none" stroke="var(--icon)"/></svg>
        <svg width="20" height="20" viewBox="0 0 20 20"><circle cx="10" cy="10" r="8.5" fill="none" stroke="var(--icon)" stroke-width="1.3"/><circle cx="10" cy="10" r="4.5" fill="none" stroke="var(--icon)"/><path d="M5.5 10h9" stroke="var(--icon)"/></svg>
        <svg width="20" height="20" viewBox="0 0 20 20"><circle cx="10" cy="10" r="8.5" fill="none" stroke="var(--icon)" stroke-width="1.3"/><circle cx="10" cy="10" r="2.5" fill="var(--icon)"/></svg>
        <svg width="20" height="20" viewBox="0 0 20 20"><circle cx="10" cy="10" r="8.5" fill="none" stroke="var(--icon)" stroke-width="1.3"/><circle cx="10" cy="10" r="2.5" fill="var(--icon)"/></svg>
        <svg width="20" height="20" viewBox="0 0 20 20"><circle cx="10" cy="10" r="8.5" fill="none" stroke="var(--icon)" stroke-width="1.3"/><circle cx="10" cy="10" r="2.5" fill="var(--icon)"/></svg>
      </div>
    </div>

    <div class="contact">
      <p class="contact__name">Dennis Halvorsen</p>
      <p class="contact__title">OWNER</p>
      <p class="contact__line">1.888.555.0162</p>
      <p class="contact__line">dennis.h@corvantsys.example</p>
      <p class="contact__line contact__line--web">www.corvantsys.example</p>
      <p class="contact__line contact__line--social">linkora.example/corvantsys</p>
      <p class="contact__line contact__line--social">chirpline.example/corvantsys</p>
      <p class="contact__line contact__line--social">pinboardly.example/corvantsys</p>
    </div>

    <div class="card__divider"></div>

    <div class="identity">
      <p class="wordmark">Corvant Systems</p>
      <p class="address">512 Brindlemoor Rd Unit C<br>Merrow Hollow<br>QX 02871</p>
    </div>
  </section>

  <section class="card card--front" aria-label="Business card front">
    <div class="card__band"></div>
    <p class="wordmark">Corvant Systems</p>
  </section>
</body>
</html>
```